依頼詳細
ぜひ頼んでみたい!!!と思ってくださるような
思い切りのいいランディングページをお願いいたします。

こんな資料がほしい!写真がほしい!動画もつけたい!
などがあればお気軽にお問い合わせください。
自由に最高のランディングページを作ってください。

参考はこちらのようなページですが
http://kumori-hitsuji.com/works/logodesign/
文字ばかりではなく、画像多めの
華やかでワクワクさせるような感じでお願いいたします。
「日本の美」を意識したデザインを希望します。
サイトURL
http://blog.tamarisu.jp/nekai/
ページ数
1ページ
希望イメージ
シンプル 複雑
単色 カラフル
暗い 明るい
日常 高級
遊び心 厳粛
未来的 伝統的
女性的 男性的
希望する色
日本をイメージさせる華やかなデザインをお願いいたします。
補足説明
ブログのロゴデザインのリンクから
今回作るランディングページへリンクしたいと考えています。
ランディングページ用の文章・画像
ご自由にブランディングして大丈夫です。
その場合は拝見させてください。
過去のブログの画像からも使って構いません。
http://fldr.example/7TxkWzR
サーバーはありますので、WEBデザインだけお願いいたします。
過去作品(インテリア用作品)
http://fldr.example/4GhvbQn

お仕事ロゴデザインサンプルなど
http://fldr.example/9JwcuLd

メディア掲載プロモーション用写真
http://fldr.example/2RpsyKe
素晴らしいデザインありがとうございました!!
どれも良いとおもっていまして
甲乙つけがたいです。
正直とても迷っているところで、延長させていただきました。

・インテリア作品
・ロゴデザインと
・プロフ写真も出します。
日本をイメージさせるデザインでお願いいたします。

ロゴデザインとインテリア用の作品が
混同されないようなご配慮をお願いいたします。
再開させていただきました。
華やかな日本をイメージさせるものにしたいです。
背景の一部に
・平安料紙切り継ぎ柄
・和紙柄
・着物柄
を取り入れて豪華なイメージにしていただきたいです。
ワークはロゴデザインを頼みたくなるような流れでお願いいたします。
金額の表示はやめることにします。
中盤や、最後に何回か
大きなボタンを入れてクリックしやすくしてほしいです。
どうぞよろしくお願いいたします。
平安調の継料紙が見当たらないとのご意見いただきました。
貴重なご意見をありがとうございます。

ワンポイントで
桜・和紙・千代紙・和柄・着物・着物帯柄など
素材がなければ無理のない程度でお願いいたします。

赤・桃色・日本を感じさせるようなデザインをお任せします。
下地背景は目に見やすい白を希望します。
ワークの順番やランディングの流れ等は
各自のデザインセンスにおまかせします。

メディア掲載も入れてもらってもかまいません。
お客様から信用を得られるようお願いしたいです。
経歴はブログをご覧ください。(抜粋して掲載を)

書道インテリア作品やロゴを多めに入れて、見栄え良くお願いします。
必要なものがございましたら用意できます。
メッセージでお声かけてください。
お待たせしています。
ミラノから帰国しました。
ブログに写真追加しました。

申し込みフォームまたは
ボタンを多めで途中でも押せるような
ランディングページをお願いいたします。

初心者でもわかりやすい、
目に見えて流れがわかるページでお願いいたします。

そろそろ決めていきたいと思っています。
フィーリングが合うデザイナーさんの
素敵な作品をお待ちしています。
どうぞよろしくお願いいたします。

良いデザインばかりだったので
迷いましたが、ずっと使えそうなデザインのものにしました。

素晴らしいご提案をありがとうございました!
また、素敵なデザインをよろしくお願いいたします。

```html
<!DOCTYPE html>
<html lang="ja">
<head>
<meta charset="utf-8">
<title>書家 森川紗月 筆文字ロゴデザイン</title>
<link rel="stylesheet" href="https://fonts.googleapis.com/css2?family=Noto+Serif+JP:wght@400;700;900&family=Shippori+Mincho+B1:wght@700;800&display=swap">
<style>
:root{
  --paper:#fbf8f2;
  --red:#c8161d;
  --deep-red:#9e0f17;
  --pink:#e77a93;
  --soft-pink:#f3c3cd;
  --gold:#c9a24a;
  --soft-gold:#e8d49a;
  --fan:#eadcc0;
  --fan-edge:#c7ae7d;
  --ink:#1b1714;
  --brown:#4a3424;
  --text:#2d2520;
}
*{box-sizing:border-box;margin:0;padding:0}
html,body{width:1200px;height:3748px;overflow:hidden}
body{
  position:relative;
  background:var(--paper);
  font-family:"Noto Serif JP",serif;
  color:var(--text);
}
.abs{position:absolute}

/* kimono pattern margins */
.kimono-panel{position:absolute;width:150px}
.kimono-panel.left{left:0;border-radius:0 60px 60px 0}
.kimono-panel.right{right:0;border-radius:60px 0 0 60px}
.tone-red{background:linear-gradient(180deg,#d83a45,var(--red) 45%,#e6808f)}
.tone-pink{background:linear-gradient(180deg,var(--soft-pink),var(--pink) 50%,#f2b6c2)}
.tone-gold{background:linear-gradient(180deg,var(--soft-gold),var(--gold) 50%,#e2c98a)}
.tone-mix{background:linear-gradient(180deg,var(--red),var(--pink) 40%,var(--gold) 75%,var(--red))}

.title-mark{left:450px;top:30px;width:300px;height:240px;border-radius:24px;
  background:linear-gradient(135deg,#3a322c,#1b1714 60%,#2a2420)}
.lead{left:0;width:1200px;text-align:center;font-weight:900}
.lead-1{top:290px;font-size:30px;color:var(--red)}
.lead-1 .name{color:var(--ink);font-size:34px}
.lead-2{top:336px;font-size:26px;color:var(--deep-red)}
.lead-2 em{font-style:normal;color:var(--red);font-size:30px}

.fan{position:absolute}
.fan svg{width:100%;height:100%;display:block}
.heading{font-family:"Shippori Mincho B1",serif;font-weight:800;color:var(--red)}

.photo{position:absolute;border:6px solid #fff;box-shadow:0 4px 14px rgba(0,0,0,.25)}
.profile-photo{left:180px;top:420px;width:410px;height:260px;background:linear-gradient(135deg,#3a2a22,#6b4b38 55%,#1b1714)}
.profile-text{left:650px;top:420px;width:370px}
.profile-text h2{font-size:34px;text-align:center;margin-bottom:14px}
.profile-text p{font-size:15px;line-height:1.8}
.history{margin-top:14px;font-size:14px;line-height:1.75}
.history li{list-style:none}

.contact-tab{left:1100px;top:600px;width:90px;height:180px;border-radius:45px;background:var(--red);
  color:#fff;writing-mode:vertical-rl;font-weight:700;font-size:22px;display:flex;align-items:center;justify-content:center;letter-spacing:.15em;box-shadow:0 3px 10px rgba(0,0,0,.3)}

.worries{left:170px;top:860px;width:620px}
.worries h2{font-size:38px;margin-bottom:18px}
.worries li{list-style:none;font-size:28px;font-weight:700;line-height:1.65}
.worries li b{color:var(--red)}

.brush-heading{left:620px;top:1095px;font-size:27px;width:420px;text-align:center}
.brush-photo{left:200px;top:1160px;width:400px;height:210px;background:linear-gradient(160deg,#f1ece4,#cfc6b8 40%,#2a2420)}
.brush-text{left:660px;top:1150px;width:350px;font-size:15px;line-height:1.85}
.brush-text b{color:var(--red)}

.works{left:160px;top:1390px;width:880px;height:500px;background:#fff;border:1px solid #d9cdb8;box-shadow:0 3px 12px rgba(0,0,0,.12)}
.works-label{left:20px;top:14px;font-size:16px;font-weight:700;color:var(--brown)}
.works-main{left:30px;top:56px;width:380px;height:400px;border:1px solid #e2d8c6;
  background:linear-gradient(160deg,#ffffff 0%,#f4f0ea 35%,#b9b1a6 60%,#f4f0ea 85%,#fff)}
.works-grid{left:440px;top:56px;width:410px;display:grid;grid-template-columns:1fr 1fr;gap:16px}
.works-grid div{height:122px;border:1px solid #e2d8c6;background:linear-gradient(135deg,#fff 10%,#cfc7bc 45%,#4a423c 55%,#d8d0c4 65%,#fff 90%)}
.works-grid div.accent{background:linear-gradient(135deg,#fff 10%,#e9b8be 45%,var(--red) 55%,#e9b8be 65%,#fff 90%)}
.works-dots{left:0;width:880px;top:472px;display:flex;justify-content:center;gap:10px}
.works-dots i{width:12px;height:12px;border-radius:50%;background:#d6cbb6}
.works-dots i:first-child{background:var(--red)}

.collab-heading{left:180px;top:1925px;font-size:32px}
.collab-text{left:180px;top:1980px;width:410px;font-size:15px;line-height:1.85}
.collab-photo{left:620px;top:1950px;width:380px;height:260px;background:linear-gradient(135deg,#f4eeee,#c8161d 55%,#5a0a10)}

.voice{left:380px;top:2250px;width:620px}
.voice h2{font-size:32px;text-align:center;margin-bottom:14px}
.voice li{list-style:none;font-size:15px;line-height:1.85}

.world{left:200px;top:2640px;width:520px}
.world h2{font-size:34px;margin-bottom:16px}
.world li{list-style:none;font-size:16px;line-height:1.9}
.world-photo{left:740px;top:2650px;width:300px;height:300px;background:linear-gradient(160deg,#e8e4df,#c8161d 50%,#2a2024)}

.steps{left:180px;top:2980px;width:840px;height:200px;
  background:linear-gradient(180deg,#4a4440,#1b1714 35%,#1b1714 70%,#3a3430);
  border-radius:14px 40px 14px 40px;display:flex;justify-content:center;align-items:center;gap:40px}
.step{color:#fff;display:flex;align-items:center;gap:6px}
.step .num{font-family:"Shippori Mincho B1",serif;font-size:90px;font-weight:800}
.step .label{writing-mode:vertical-rl;font-size:26px;font-weight:700;letter-spacing:.1em}
.steps-text{left:240px;top:3200px;width:720px;font-size:15px;line-height:1.85}
.cta{left:240px;top:3270px;width:720px;font-size:24px;font-weight:900;color:var(--ink);line-height:1.6}

.form{left:240px;top:3360px;width:720px}
.form-head{background:var(--ink);color:#fff;font-weight:700;font-size:20px;padding:8px 20px;border-radius:6px 6px 0 0}
.form table{width:100%;border-collapse:collapse;background:#fff}
.form th{width:200px;background:#efe6d4;font-size:15px;text-align:left;padding:10px 14px;border:1px solid #d7c9ad;font-weight:700}
.form td{border:1px solid #d7c9ad;padding:8px 12px}
.form td span{display:block;height:22px;border:1px solid #c9bba0;background:#fcfaf6}
.form td span.tall{height:60px}
.submit{display:block;margin:16px auto 0;width:300px;text-align:center;background:var(--red);color:#fff;font-size:22px;font-weight:700;padding:12px;border-radius:30px}
</style>
</head>
<body>

<!-- kimono pattern margins -->
<div class="kimono-panel left tone-mix" style="top:0;height:400px" role="img" aria-label="牡丹と菊の着物柄"></div>
<div class="kimono-panel left tone-red" style="top:420px;height:300px" role="img" aria-label="赤い牡丹の着物柄"></div>
<div class="kimono-panel left tone-pink" style="top:960px;height:340px" role="img" aria-label="桜の千代紙柄"></div>
<div class="kimono-panel left tone-gold" style="top:1700px;height:200px" role="img" aria-label="金の菊の着物柄"></div>
<div class="kimono-panel left tone-mix" style="top:2130px;height:420px" role="img" aria-label="菊と桜の着物柄"></div>
<div class="kimono-panel left tone-red" style="top:2620px;height:300px" role="img" aria-label="牡丹の着物柄"></div>
<div class="kimono-panel left tone-gold" style="top:3060px;height:240px" role="img" aria-label="金の菊の着物柄"></div>
<div class="kimono-panel left tone-pink" style="top:3520px;height:228px" role="img" aria-label="桜の着物柄"></div>

<div class="kimono-panel right tone-mix" style="top:0;height:420px" role="img" aria-label="牡丹と菊の着物柄"></div>
<div class="kimono-panel right tone-gold" style="top:820px;height:260px" role="img" aria-label="金の菊の着物柄"></div>
<div class="kimono-panel right tone-red" style="top:1090px;height:240px" role="img" aria-label="赤い菊の着物柄"></div>
<div class="kimono-panel right tone-mix" style="top:1880px;height:440px" role="img" aria-label="菊の着物柄"></div>
<div class="kimono-panel right tone-pink" style="top:2560px;height:260px" role="img" aria-label="桜の着物柄"></div>
<div class="kimono-panel right tone-red" style="top:2940px;height:300px" role="img" aria-label="牡丹の着物柄"></div>
<div class="kimono-panel right tone-mix" style="top:3320px;height:428px" role="img" aria-label="牡丹と菊の着物柄"></div>

<!-- header -->
<div class="abs title-mark" role="img" aria-label="毛筆で大きく書かれた一文字の書作品"></div>
<p class="abs lead lead-1">世界で活躍中! <span class="name">書家 森川紗月</span> が心を込めてお書きします。</p>
<p class="abs lead lead-2">あなたに贈る毛筆の芸術作品。<em>お客様に感動を与えます!</em></p>

<!-- profile -->
<div class="fan" style="left:620px;top:385px;width:430px;height:460px">
<svg viewBox="0 0 430 460" preserveAspectRatio="none"><path d="M10,40 Q215,-20 420,40 L390,450 Q215,420 40,450 Z" fill="var(--fan)" stroke="var(--fan-edge)" stroke-width="3"/></svg>
</div>
<div class="photo profile-photo" role="img" aria-label="筆で作品を書く書家の写真"></div>
<section class="abs profile-text">
  <h2 class="heading">書家の紹介</h2>
  <p>幼少より書に親しみ、伝統の筆致を大切にしながら現代の暮らしに寄り添う作品を制作。国内外の展示会で高い評価を受けています。</p>
  <ul class="history">
    <li>2010年　書道師範の資格を取得</li>
    <li>2012年　東京にて初の個展を開催</li>
    <li>2014年　パリの展示会に作品を出品</li>
    <li>2015年　企業ロゴの筆文字制作を開始</li>
    <li>2016年　ミラノにて作品展示</li>
    <li>2017年　海外ホテルへ作品を納品</li>
  </ul>
</section>

<div class="abs contact-tab">お問い合わせ</div>

<!-- worries -->
<div class="fan" style="left:150px;top:830px;width:640px;height:290px">
<svg viewBox="0 0 640 290" preserveAspectRatio="none"><path d="M10,30 Q320,-10 630,30 L570,280 Q320,250 70,280 Z" fill="var(--fan)" stroke="var(--fan-edge)" stroke-width="3"/></svg>
</div>
<section class="abs worries">
  <h2 class="heading">こんなお悩みありませんか?</h2>
  <ul>
    <li>・商品やサービスの<b>ブランディング</b>を<br>強化したい。</li>
    <li>・他社との差別化が図りたい。</li>
    <li>・海外進出を検討している。</li>
  </ul>
</section>

<!-- brush logo -->
<div class="fan" style="left:620px;top:1080px;width:420px;height:300px">
<svg viewBox="0 0 420 300" preserveAspectRatio="none"><path d="M10,20 Q210,-10 410,20 L380,290 Q210,270 40,290 Z" fill="var(--fan)" stroke="var(--fan-edge)" stroke-width="3"/></svg>
</div>
<h2 class="abs heading brush-heading">ブランドロゴに筆文字デザイン</h2>
<div class="photo brush-photo" role="img" aria-label="半紙に筆で文字を書く手元の写真"></div>
<p class="abs brush-text" style="top:1150px">一筆ごとに想いを込めた<b>筆文字ロゴ</b>は、お客様の印象に深く残ります。伝統的な書の美しさと現代のデザインを融合し、<b>世界に通用するブランド</b>を創り上げます。商品名や店名を毛筆でお書きし、お客様だけの特別なロゴを制作いたします。</p>

<!-- works -->
<section class="abs works">
  <p class="abs works-label">事例紹介</p>
  <div class="abs works-main" role="img" aria-label="毛筆で書いた店名ロゴの制作事例"></div>
  <div class="abs works-grid">
    <div role="img" aria-label="筆文字ロゴの制作事例"></div>
    <div role="img" aria-label="筆文字ロゴの制作事例"></div>
    <div role="img" aria-label="筆文字ロゴの制作事例"></div>
    <div class="accent" role="img" aria-label="赤い落款入り筆文字ロゴの制作事例"></div>
    <div role="img" aria-label="筆文字ロゴの制作事例"></div>
    <div role="img" aria-label="筆文字ロゴの制作事例"></div>
  </div>
  <div class="abs works-dots"><i></i><i></i><i></i></div>
</section>

<!-- collaboration -->
<h2 class="abs heading collab-heading">コラボレーション企画も可能です。</h2>
<p class="abs collab-text">企業様や作家様とのコラボレーション企画にも対応いたします。商品パッケージ、店舗の内装、イベントでの揮毫パフォーマンスなど、ご要望に合わせた書の演出をご提案します。まずはお気軽にご相談ください。</p>
<div class="photo collab-photo" role="img" aria-label="赤と白の書作品によるコラボレーション展示の写真"></div>

<!-- voices -->
<div class="fan" style="left:340px;top:2230px;width:700px;height:340px">
<svg viewBox="0 0 700 340" preserveAspectRatio="none"><path d="M10,30 Q350,-10 690,30 L620,330 Q350,300 80,330 Z" fill="var(--fan)" stroke="var(--fan-edge)" stroke-width="3"/></svg>
</div>
<section class="abs voice">
  <h2 class="heading">お客様の声</h2>
  <ul>
    <li>■想像以上の仕上がりで、お店の雰囲気が一気に華やかになりました。</li>
    <li>■海外のお客様からも大変好評で、ブランドの顔として愛用しています。</li>
    <li>■丁寧な打合せで要望をしっかり汲み取っていただき感謝しています。</li>
    <li>■新商品のロゴを依頼し、売上が伸びました。また依頼したいです。</li>
    <li>■筆文字の力強さと優しさが伝わる、唯一無二のロゴになりました。</li>
  </ul>
</section>

<!-- world -->
<div class="fan" style="left:170px;top:2610px;width:570px;height:330px">
<svg viewBox="0 0 570 330" preserveAspectRatio="none"><path d="M10,30 Q285,-10 560,30 L500,320 Q285,290 70,320 Z" fill="var(--fan)" stroke="var(--fan-edge)" stroke-width="3"/></svg>
</div>
<section class="abs world">
  <h2 class="heading">世界で選ばれています</h2>
  <ul>
    <li>◆フランス・パリ　展示作品を制作</li>
    <li>◆イタリア・ミラノ　作品展に出展</li>
    <li>◆アメリカ・ニューヨーク　ホテルへ納品</li>
    <li>◆国内企業様　筆文字ロゴを多数制作</li>
    <li>◆雑誌・メディアにて作品が紹介されました</li>
  </ul>
</section>
<div class="photo world-photo" role="img" aria-label="着物姿で作品を持つ書家のプロフィール写真"></div>

<!-- steps -->
<div class="abs steps" role="group" aria-label="ご依頼の流れ">
  <div class="step"><span class="num">1</span><span class="label">面会</span></div>
  <div class="step"><span class="num">2</span><span class="label">打合せ</span></div>
  <div class="step"><span class="num">3</span><span class="label">提案</span></div>
  <div class="step"><span class="num">4</span><span class="label">納品</span></div>
</div>
<p class="abs steps-text">ヒアリングからイメージのご提案、清書、納品まで丁寧に対応いたします。データ納品も可能です。</p>
<p class="abs cta">まずはお気軽にご相談ください。<br>担当者より折り返しご連絡させて頂きます。</p>

<!-- form -->
<section class="abs form">
  <div class="form-head">お申し込みフォーム</div>
  <table>
    <tr><th>お名前</th><td><span></span></td></tr>
    <tr><th>ふりがな</th><td><span></span></td></tr>
    <tr><th>会社名</th><td><span></span></td></tr>
    <tr><th>メールアドレス</th><td><span></span></td></tr>
    <tr><th>電話番号</th><td><span></span></td></tr>
    <tr><th>ご相談内容</th><td><span class="tall"></span></td></tr>
  </table>
  <span class="submit">送信する</span>
</section>

</body>
</html>
```